Harbor Data Services
• 13 avril 2011 17:34 Vorin
For the back design we want the lower right hand corner design with the single logo in the center of the card and text indicated in previous note.
Thanks for the great work,
BKW
• 13 avril 2011 17:21 Vorin
This is important -- we need to have changes made to the winning design - Draft #68. The following needs to be updated before final artwork is sent to us.
1. The text on the back needs to read: You can partner with the most caring technology services firm in the world.
2. Change website icon to globe, don't want current "eye" icon. See draft #58 for example.
3. We don't like or want any yellow type.
6. Name and title change font should be the same as Draft #58.
7. Name and title should be lower case except for first letter of word.
Thanks, BKW
• 8 avril 2011 11:14 Vorin
Thanks for the great updates and new concepts. Mirabelcanta, we really appreciate all the variations you have provided. Our logo has the the sun on the left and our company name to the right, so it is incorrectly presented on our website. I have also uploaded our actual logo. Draft #58 remains our favorite. Draft #79 is the vertical representation and we really like it also. For the back, we really like the shadow copy of Draft #71 where the guys helping each other are in the background. Not sure the logo needs to be repeated on the back if the shadow copy is there. Centering the You can hire on the back is fine. We also like the bright blue of Draft #60 has on the back. We don't want any text in the bright yellow or "highlighter" color.
• 7 avril 2011 13:52 Vorin
Draft #58 is our current favorite. We do prefer the round icons on the bottom left design. One more general design preference is that company logo should be above the person's name. We do like draft #65, but it needs to be revised per the direction of our last comment - thanks.
• 7 avril 2011 13:39 Vorin
Thanks for the new submissions and great work. To help provide clarity on our preferences here are some guidelines.
1. Given our logo, corners should be rounded, not square.
2. Our company names does not need to be on the back of the card. Logo should be there, but blank space for people to write their own info is fine with us.
3. Icons should be used for address & phone info - don't use text or abbreviations.
4. We want text to be lower case except for first letter to be consistent with our logo.
5. Blue is our preferred color for the back of the card.
6. The leading back design is Draft #47.
• 5 avril 2011 19:32 Vorin
Thanks for the great work and updated submissions. Draft #47 remains our favorite. We like the round icons, although we are concerned they are so small that people won't be able to tell which number is the cell phone, etc. We also like the bottom left version the best. On Draft #34, this is our 2nd favorite. If you could drop the Building Every Future from our logo and use the round icons, we would like to see this design revised. We're very impressed with the work being done on our behalf.
Draft #17 by kelpwindow is a derivative of #16 by Plumdex, therefore has been taken down.
• 4 avril 2011 22:27 Vorin
We uploaded our actual logo. The leg on the lower person should in the logo should not have their leg outside of the circle. On my cell phone number there needs a dash between 352 & 6174. Minor details, but thought we should point them out now. Draft #28 remains our favorite - thanks.
• 4 avril 2011 17:24 Vorin
We also really like the rounded corners on the cards as shown in Draft #28 as our logo is round and this seems to be a natural extension of our logo - thanks.
• 4 avril 2011 17:16 Vorin
Our compliments to all for the great designs - thanks. Our favorite is Draft #28. We like the design in the top left hand corner the best of all submitted to date. We like the separation between name and contact info and the use of the 3 primary colors in our logo. We like the solid blue back with our brand promise reversed as shown in Draft #28.
• 4 avril 2011 14:56 mirabelcanta
PS
I don’t see new additions in the brief and left with the impression that we must made a business card. If I'm misunderstood will do and other stationery.
• 4 avril 2011 14:42 mirabelcanta
Dear JD,
Thank you for the evaluation and fast feedback. Please say more also about the face of the BC. And what you do not like in drafts - maybe it's more important to improve the design according to your needs.
Regards
Mira
• 3 avril 2011 18:48 Vorin
Thanks for the great submissions. You all are very talented. Of the drafts submitted, #9 is our favorite followed closely by #8. We really like the rounded corners and the name being centered on the left. We like the solid blue back side of the card in #8 and not sure about the circles on the back in #9. We also really like our tag line to be reversed on the front. We also really like the yellow and grey accent lines above the reversed text with our tag line #10.
• 3 avril 2011 14:16 Feshi
Hello JD,
sir i cant get the logo and design material.. gtom the download??? plz let me know how can i ...i saw ur logo on the site ...but i need a Ai file
thanks feshi
• 2 avril 2011 21:36 Vorin
Thanks for your submission. I like #1 the best. I like the reverse on the bottom of the card and the icons for info vs. words. We are changing our tag line in the current logo from Building Every Future Through Systems to Standing By Those Who Serve. The tag line can stay at the bottom of the card and be eliminated below the logo. On the back of the card we want it to say: You can hire the most caring technology services firm in the world.

```html
<!DOCTYPE html>
<html lang="en">
<head>
<meta charset="utf-8">
<title>Harbor Data Services – Business Card</title>
<link rel="stylesheet" href="https://fonts.googleapis.com/css2?family=Arimo:wght@700&family=Tinos:wght@400;700&display=swap">
<style>
  :root {
    --page: #ffffff;
    --blue-deep: #0a7fc4;
    --blue-bright: #2cb3ee;
    --blue-light: #7fd4f7;
    --brand-ink: #1d2a4a;
    --accent-blue: #1a8ad0;
    --text-dark: #2a2a2a;
    --white: #ffffff;
    --grey-light: #f4f4f4;
    --grey-mid: #d9d9d9;
    --mark-grey: #b9bec4;
  }
  * { margin: 0; padding: 0; box-sizing: border-box; }
  html, body { width: 1200px; height: 600px; overflow: hidden; background: var(--page); }
  .canvas { position: relative; width: 1200px; height: 600px; }

  .card {
    position: absolute; top: 298px; width: 420px; height: 236px;
    border-radius: 18px; overflow: hidden;
    box-shadow: 0 3px 6px rgba(0,0,0,.25);
  }
  .card-back { left: 178px; background: radial-gradient(ellipse at 50% 50%, var(--blue-bright) 0%, var(--blue-deep) 100%); }
  .card-front { left: 643px; background: linear-gradient(180deg, var(--white) 0%, var(--grey-light) 60%, var(--grey-mid) 100%); }
  .card svg.decor { position: absolute; inset: 0; }

  .brand { position: absolute; display: flex; align-items: center; gap: 8px; }
  .brand-dot { width: 64px; height: 64px; border-radius: 50%; background: var(--mark-grey); flex: none; }
  .brand-name {
    font-family: "Arimo", sans-serif; font-weight: 700; font-size: 19px;
    line-height: 19px; color: var(--brand-ink); width: 110px;
  }
  .card-back .brand { left: 50px; top: 52px; }
  .card-front .brand { left: 8px; top: 58px; }

  .promise {
    position: absolute; left: 0; right: 0; top: 152px; text-align: center;
    font-family: "Tinos", serif; font-weight: 700; font-size: 13px;
    line-height: 24px; color: var(--white);
  }
  .tagline {
    position: absolute; left: 18px; top: 130px;
    font-family: "Tinos", serif; font-weight: 700; font-size: 13px; color: var(--accent-blue);
  }

  .person { position: absolute; right: 14px; top: 20px; text-align: right; font-family: "Tinos", serif; }
  .person-name { font-size: 17px; color: var(--accent-blue); font-variant: small-caps; letter-spacing: .5px; }
  .person-title { font-size: 10px; font-weight: 700; color: var(--text-dark); margin-top: 2px; }

  .contact { position: absolute; right: 14px; top: 78px; text-align: right;
    font-family: "Tinos", serif; font-size: 9.5px; line-height: 12px; color: var(--text-dark); }
  .contact-group { margin-bottom: 8px; display: flex; gap: 5px; justify-content: flex-end; }
  .contact-group svg { flex: none; margin-top: 1px; }
</style>
</head>
<body>
<main class="canvas">

  <section class="card card-back">
    <svg class="decor" viewBox="0 0 420 236" aria-hidden="true">
      <g fill="none" stroke="var(--blue-light)" stroke-opacity=".45">
        <path d="M-40 -20 Q60 118 -40 256" stroke-width="26"/>
        <path d="M-10 -20 Q100 118 -10 256" stroke-width="10"/>
        <path d="M460 -20 Q360 118 460 256" stroke-width="26"/>
        <path d="M430 -20 Q320 118 430 256" stroke-width="10"/>
      </g>
    </svg>
    <div class="brand">
      <span class="brand-dot"></span>
      <span class="brand-name">Harbor Data Services</span>
    </div>
    <p class="promise">You can hire the most caring<br>technology services firm in the world</p>
  </section>

  <section class="card card-front">
    <svg class="decor" viewBox="0 0 420 236" aria-hidden="true">
      <path d="M0 0 H40 Q-10 118 40 236 H0 Z" fill="var(--blue-deep)"/>
      <path d="M52 0 Q0 118 52 236" fill="none" stroke="var(--blue-bright)" stroke-width="8"/>
      <path d="M66 0 Q18 118 66 236" fill="none" stroke="var(--blue-light)" stroke-width="3"/>
    </svg>
    <div class="brand">
      <span class="brand-dot"></span>
      <span class="brand-name">Harbor Data Services</span>
    </div>
    <p class="tagline">Standing by those who serve</p>

    <div class="person">
      <p class="person-name">Dalen R. Okafor</p>
      <p class="person-title">Managing Principal</p>
    </div>

    <div class="contact">
      <div class="contact-group">
        <svg width="10" height="10" viewBox="0 0 10 10"><path d="M5 0 L10 5 H8.5 V10 H1.5 V5 H0 Z" fill="var(--accent-blue)"/></svg>
        <div>4120 W. Linden Ave.<br>Brookhaven, KS 66790</div>
      </div>
      <div class="contact-group">
        <svg width="10" height="10" viewBox="0 0 10 10"><path d="M2 0 L4 2.5 L3 4 Q4.5 6 6 7 L7.5 6 L10 8 L8.5 10 Q2 9 0 1.5 Z" fill="var(--accent-blue)"/></svg>
        <div>555-214-3090<br>555-352-6174<br>F:555-418-2207</div>
      </div>
      <div class="contact-group">
        <svg width="10" height="10" viewBox="0 0 10 10"><rect x="0" y="2" width="10" height="7" fill="var(--accent-blue)"/><path d="M0 2 L5 6 L10 2" fill="none" stroke="var(--white)" stroke-width="1"/></svg>
        <div>dalen@hds-mail.com<br>www.hds-mail.com</div>
      </div>
    </div>
  </section>

</main>
</body>
</html>
```